Consulting company business cards

We have a base design, but would be willing to update. We have a new logo/"tag" that needs to be added. Current business card design is attached for reference into our "style."

Industry/Entity Type

Business

Contact Information for Business Card

Should contain name and title, office number, mobile number if appropriate, e-mail, website, physical address, and company logo.

Font styles to use
Other font styles liked:
• See current card design on DrovankBCard

Colors
0455a3
85acd3
aaaaaa

Requirements
Must have
• Our colors are navy blue, gray, and a lighter blue
Nice to have
• Design that I can easily drop in new names/titles as we hire employees.

```html
<!DOCTYPE html>
<html lang="en">
<head>
<meta charset="utf-8">
<title>Harrow business cards</title>
<link rel="stylesheet" href="https://fonts.googleapis.com/css2?family=Arimo:wght@400;700&display=swap">
<style>
  :root {
    --stage: #3b3431;
    --card: #151617;
    --card-edge: #1d1e20;
    --navy: #0455a3;
    --navy-deep: #1f4468;
    --light-blue: #85acd3;
    --gray: #aaaaaa;
    --white: #f2f2f2;
  }
  * { margin: 0; padding: 0; box-sizing: border-box; }
  html, body { width: 1200px; height: 864px; overflow: hidden; }
  body {
    background: var(--stage);
    font-family: "Arimo", Arial, sans-serif;
    position: relative;
  }
  .card {
    position: absolute;
    width: 540px;
    height: 308px;
    background: var(--card);
    border: 1px solid var(--card-edge);
    border-radius: 3px;
    box-shadow: 0 10px 30px rgba(0,0,0,.45);
  }
  .card--front { left: 70px; top: 90px; }
  .card--back  { left: 590px; top: 466px; }

  .brand { position: absolute; }
  .brand__row { display: flex; align-items: center; gap: 14px; }
  .brand__name {
    font-weight: 700;
    color: var(--navy-deep);
    letter-spacing: 2px;
    line-height: 1;
  }
  .brand__dot {
    border-radius: 50%;
    background: var(--light-blue);
    flex: none;
  }
  .brand__tagline {
    color: var(--gray);
    font-weight: 700;
    letter-spacing: 1.2px;
    text-transform: uppercase;
    margin-top: 4px;
  }

  .card--front .brand { left: 90px; top: 92px; }
  .card--front .brand__name { font-size: 62px; }
  .card--front .brand__dot { width: 54px; height: 54px; }
  .card--front .brand__tagline { font-size: 15px; }
  .front__web {
    position: absolute;
    left: 90px;
    top: 222px;
    font-size: 14px;
    letter-spacing: 5px;
    color: var(--gray);
  }

  .card--back .brand { left: 34px; top: 108px; }
  .card--back .brand__name { font-size: 42px; }
  .card--back .brand__dot { width: 38px; height: 38px; }
  .card--back .brand__tagline { font-size: 10.5px; }

  .back__divider {
    position: absolute;
    left: 300px;
    top: 46px;
    width: 1px;
    height: 216px;
    background: linear-gradient(to bottom, transparent, var(--gray), transparent);
  }
  .contact { position: absolute; left: 322px; top: 56px; color: var(--white); }
  .contact__name { font-size: 20px; color: var(--navy); }
  .contact__title { font-size: 15px; color: var(--light-blue); margin-top: 3px; }
  .contact__address { font-size: 13px; line-height: 17px; margin-top: 14px; }
  .contact__list { list-style: none; margin-top: 14px; font-size: 13.5px; }
  .contact__list li { display: flex; align-items: center; gap: 8px; height: 20px; }
  .contact__icon { width: 12px; height: 12px; flex: none; }
</style>
</head>
<body>
  <section class="card card--front" aria-label="Card front">
    <div class="brand">
      <div class="brand__row">
        <span class="brand__name">HARROW</span>
        <span class="brand__dot"></span>
      </div>
      <div class="brand__tagline">A Cloud Consulting Company</div>
    </div>
    <div class="front__web">www.harrowcloud.com</div>
  </section>

  <section class="card card--back" aria-label="Card back">
    <div class="brand">
      <div class="brand__row">
        <span class="brand__name">HARROW</span>
        <span class="brand__dot"></span>
      </div>
      <div class="brand__tagline">A Cloud Consulting Company</div>
    </div>
    <div class="back__divider"></div>
    <div class="contact">
      <div class="contact__name">Lorna Drovank</div>
      <div class="contact__title">Office Manager</div>
      <div class="contact__address">1850 N Birch Ave<br>Fairview Indiana 46011</div>
      <ul class="contact__list">
        <li>
          <svg class="contact__icon" viewBox="0 0 12 12"><path fill="#0455a3" d="M2.5 1 4.5 1 5.2 3.6 4 4.6C4.6 6 6 7.4 7.4 8L8.4 6.8 11 7.5 11 9.5C11 10.3 10.3 11 9.5 11 5 11 1 7 1 2.5 1 1.7 1.7 1 2.5 1Z"/></svg>
          555.014.2210
        </li>
        <li>
          <svg class="contact__icon" viewBox="0 0 12 12"><rect x="2" y="1" width="8" height="10" rx="1.5" fill="#0455a3"/><rect x="3.3" y="2.3" width="5.4" height="6.5" fill="#151617"/></svg>
          555.014.2271
        </li>
        <li>
          <svg class="contact__icon" viewBox="0 0 12 12"><rect x="0.5" y="2.5" width="11" height="7.5" rx="1" fill="#0455a3"/><path d="M1 3 6 7 11 3" fill="none" stroke="#151617" stroke-width="1"/></svg>
          ldrovank@harrowcloud.com
        </li>
        <li>
          <svg class="contact__icon" viewBox="0 0 12 12"><circle cx="6" cy="6" r="5.5" fill="#0455a3"/><path d="M0.5 6H11.5M6 0.5C3.5 3 3.5 9 6 11.5M6 0.5C8.5 3 8.5 9 6 11.5" fill="none" stroke="#151617" stroke-width="0.8"/></svg>
          www.harrowcloud.com
        </li>
      </ul>
    </div>
  </section>
</body>
</html>
```